Varnel Supply requires a new business card.

We are an online professional tool store.

Target Market(s)

We target the professional technician.

Industry/Entity Type

Business

Contact Information for Business Card

VarnelSupply.com.au

sales@varnelsupply.example

Requirements
Must have
• Needs to look commercial and professional
Should not have
• No Australian Colors, maps or shapes.
• No Shapes of Tools

```html
<!DOCTYPE html>
<html lang="en">
<head>
<meta charset="utf-8">
<title>Varnel Supply — Business Card</title>
<link rel="stylesheet" href="https://fonts.googleapis.com/css2?family=Questrial&display=swap">
<style>
  :root {
    --backdrop: #d9d9d9;
    --card-grey: #c9c7c6;
    --ink-black: #000000;
    --brand-blue: #2e3589;
    --accent-cyan: #1e8fc0;
    --text-dark: #111111;
  }
  * { box-sizing: border-box; margin: 0; padding: 0; }
  html, body {
    width: 1200px; height: 1200px; overflow: hidden;
    background: var(--backdrop);
    font-family: "Questrial", "Century Gothic", sans-serif;
  }
  .sheet {
    width: 1200px; height: 1200px;
    display: flex; flex-direction: column; align-items: center; justify-content: center;
    gap: 70px;
  }
  .card {
    position: relative;
    width: 840px; height: 480px;
    background: var(--card-grey);
    overflow: hidden;
    box-shadow: 0 6px 18px rgba(0,0,0,0.18);
  }
  /* Front */
  .front-band {
    position: absolute; left: 100px; right: 100px; top: 130px; height: 220px;
    background: var(--ink-black);
    display: flex; align-items: center; justify-content: center;
  }
  .front-accent {
    position: absolute; left: 0; width: 100px; top: 122px; height: 236px;
    background: var(--brand-blue);
  }
  .wordmark {
    display: flex; align-items: center; gap: 14px;
    color: var(--brand-blue);
    font-size: 40px; letter-spacing: 1px;
    white-space: nowrap;
  }
  .wordmark-dot {
    flex: none;
    width: 22px; height: 22px; border-radius: 50%;
    background: var(--accent-cyan);
  }
  /* Back */
  .back-panel {
    position: absolute; left: 75px; top: 50px; width: 330px; height: 290px;
    background: var(--ink-black);
    display: flex; align-items: center; justify-content: center;
  }
  .back-panel .wordmark { font-size: 34px; gap: 12px; }
  .back-panel .wordmark-dot { width: 18px; height: 18px; }
  .back-rule {
    position: absolute; left: 180px; top: 330px; width: 250px; height: 22px;
    background: var(--brand-blue);
  }
  .back-block {
    position: absolute; right: 60px; bottom: 0; width: 170px; height: 140px;
    background: var(--brand-blue);
  }
  .contacts {
    position: absolute; left: 440px; top: 200px;
    list-style: none;
    display: flex; flex-direction: column; gap: 24px;
    color: var(--text-dark); font-size: 23px;
    white-space: nowrap;
  }
  .contacts li { display: flex; align-items: center; gap: 12px; }
  .contacts svg { flex: none; }
</style>
</head>
<body>
<main class="sheet">
  <section class="card card-front" aria-label="Card front">
    <div class="front-accent"></div>
    <div class="front-band">
      <div class="wordmark"><span class="wordmark-dot"></span><span>Varnel Supply</span></div>
    </div>
  </section>

  <section class="card card-back" aria-label="Card back">
    <div class="back-panel">
      <div class="wordmark"><span class="wordmark-dot"></span><span>Varnel Supply</span></div>
    </div>
    <div class="back-rule"></div>
    <ul class="contacts">
      <li>
        <svg width="28" height="20" viewBox="0 0 28 20" aria-hidden="true">
          <rect x="0" y="0" width="28" height="20" fill="var(--accent-cyan)"/>
          <polyline points="0,0 14,11 28,0" fill="none" stroke="#fff" stroke-width="2"/>
        </svg>
        <span>sales@varnelsupply.example</span>
      </li>
      <li>
        <svg width="28" height="26" viewBox="0 0 28 26" aria-hidden="true">
          <circle cx="14" cy="13" r="12" fill="var(--accent-cyan)"/>
          <ellipse cx="14" cy="13" rx="5" ry="12" fill="none" stroke="#fff" stroke-width="1.5"/>
          <line x1="2" y1="13" x2="26" y2="13" stroke="#fff" stroke-width="1.5"/>
        </svg>
        <span>VarnelSupply.com.au</span>
      </li>
    </ul>
    <div class="back-block"></div>
  </section>
</main>
</body>
</html>
```